Dale Morrikan Plumbing and Heating

Need a card design for a plumbing and heating company that does service and repair, remodels, and plumbing in new construction. Please add following on back side of card; Boilers, Water heaters, Gas lines, Sump pumps, Toilet repairs, Faucet repairs, Pipe thawing, Radiant heating, New construction, Remodels.

Industry/Entity Type

Plumber

Contact Information for Business Card

Was thinking white gloss card with colored logo in middle or black glossy card with silver logo in middle. Just a thought but very open to other designs.

Requirements
Must have
• Need following on front of card;
• P(203) 321-8689
• C(203) 232-9069
• Dale Morrikan 275 Larkwell St West, Stamford, Ct 06214
• service@DrainHearth.example (plumbing in blue, heating in red)
• www.DrainHearth.example (plumbing in blue, heating in red)
• Fully Licensed and Insured
Nice to have
• Elegant design

```html
<!DOCTYPE html>
<html lang="en">
<head>
<meta charset="utf-8">
<title>Dale Morrikan Plumbing and Heating – Business Card</title>
<link rel="stylesheet" href="https://fonts.googleapis.com/css2?family=Fira+Sans:wght@300;400;700&display=swap">
<style>
  :root {
    --page-bg: #e9e6e1;
    --silver-light: #fbfbfb;
    --silver-mid: #e3e4e6;
    --silver-dark: #b9bcc0;
    --blue-deep: #123f7c;
    --blue-mid: #1d64b0;
    --blue-bright: #3d9ee0;
    --blue-text: #1c63b7;
    --red: #d3202f;
    --grey-text: #7d7f82;
    --white: #ffffff;
  }
  * { box-sizing: border-box; margin: 0; padding: 0; }
  html, body {
    width: 988px; height: 1200px; overflow: hidden;
    background: var(--page-bg);
    font-family: "Fira Sans", Arial, sans-serif;
  }
  .card {
    position: absolute;
    width: 780px; height: 452px;
    box-shadow: 0 6px 18px rgba(0,0,0,.28);
    overflow: hidden;
  }
  .card--front { left: 104px; top: 110px; }
  .card--back  { left: 104px; top: 650px; }
  .card__bg { position: absolute; inset: 0; }
  .centered { position: absolute; left: 0; right: 0; text-align: center; }

  /* front */
  .brand-mark {
    position: absolute; left: 355px; top: 40px;
    width: 70px; height: 70px; border-radius: 50%;
    background: var(--blue-mid);
  }
  .brand-name {
    top: 156px; color: var(--blue-deep);
    font-weight: 700; font-size: 30px; letter-spacing: 2px; text-transform: uppercase;
    line-height: 32px;
  }
  .brand-name span { display: block; font-size: 21px; letter-spacing: 3px; }
  .web-line {
    top: 220px; display: flex; justify-content: center; align-items: center; gap: 10px;
    font-size: 14px; font-weight: 700; color: var(--grey-text);
  }
  .web-line .rule { width: 80px; height: 1px; background: var(--grey-text); }
  .web-line .domain { color: var(--blue-text); }
  .contact { color: var(--white); }
  .contact__name { top: 286px; font-weight: 700; font-size: 27px; }
  .contact__line {
    font-weight: 300; font-size: 28px; letter-spacing: .5px;
    display: flex; justify-content: center; align-items: center; gap: 6px;
  }
  .contact__line svg { flex: none; }
  .contact__phone { top: 322px; }
  .contact__mobile { top: 358px; }
  .contact__email { top: 396px; font-size: 25px; }

  /* back */
  .tagline { top: 48px; color: var(--white); font-weight: 700; font-size: 26px; }
  .services {
    top: 160px; color: var(--blue-text); font-weight: 700; font-size: 26px;
    line-height: 49.5px;
  }
  .services li { list-style: none; }
  .diamond {
    display: inline-block; width: 10px; height: 10px; margin: 0 8px 4px;
    background: var(--red); transform: rotate(45deg);
  }
  .back-web {
    top: 376px; display: flex; justify-content: center; align-items: center; gap: 10px;
    font-size: 24px; font-weight: 700; color: var(--grey-text);
  }
  .back-web .rule { width: 150px; height: 4px; background: linear-gradient(90deg, transparent, var(--grey-text)); }
  .back-web .rule--right { background: linear-gradient(90deg, var(--grey-text), transparent); }
  .back-web .domain { color: var(--blue-text); }
</style>
</head>
<body>

<section class="card card--front" aria-label="Card front">
  <svg class="card__bg" viewBox="0 0 780 452" width="780" height="452" aria-hidden="true">
    <defs>
      <linearGradient id="frontSilver" x1="0" y1="0" x2="1" y2="0">
        <stop offset="0" stop-color="#c9cbce"/>
        <stop offset=".35" stop-color="#fdfdfd"/>
        <stop offset=".7" stop-color="#f2f3f4"/>
        <stop offset="1" stop-color="#c4c6c9"/>
      </linearGradient>
      <linearGradient id="frontBand" x1="0" y1="0" x2="0" y2="1">
        <stop offset="0" stop-color="#3d9ee0"/>
        <stop offset=".35" stop-color="#1d64b0"/>
        <stop offset=".8" stop-color="#123f7c"/>
        <stop offset="1" stop-color="#2f58a6"/>
      </linearGradient>
      <linearGradient id="frontStripe" x1="0" y1="0" x2="1" y2="0">
        <stop offset="0" stop-color="#8d9094"/>
        <stop offset=".5" stop-color="#ffffff"/>
        <stop offset="1" stop-color="#8d9094"/>
      </linearGradient>
    </defs>
    <rect width="780" height="452" fill="url(#frontSilver)"/>
    <path d="M0 268 Q390 232 780 262 L780 276 Q390 250 0 284 Z" fill="url(#frontStripe)"/>
    <path d="M0 284 Q390 250 780 276 L780 452 L0 452 Z" fill="url(#frontBand)"/>
  </svg>

  <div class="brand-mark" aria-hidden="true"></div>
  <h1 class="centered brand-name">Dale Morrikan<span>Plumbing and Heating</span></h1>
  <p class="centered web-line"><i class="rule"></i><span>www.<span class="domain">DrainHearth</span>.example</span><i class="rule"></i></p>

  <div class="contact">
    <p class="centered contact__name">Dale Morrikan</p>
    <p class="centered contact__line contact__phone">
      <svg width="22" height="26" viewBox="0 0 22 26" aria-label="Phone"><path d="M5 2 L9 2 L10 8 L7 10 Q9 16 14 19 L17 16 L21 18 L20 23 Q14 25 8 19 Q2 12 3 4 Z" fill="none" stroke="#fff" stroke-width="2" stroke-linejoin="round"/></svg>
      (203) 555-0147
    </p>
    <p class="centered contact__line contact__mobile">
      <svg width="20" height="28" viewBox="0 0 20 28" aria-label="Mobile"><rect x="2" y="2" width="16" height="24" rx="2" fill="none" stroke="#fff" stroke-width="2"/><line x1="8" y1="22" x2="12" y2="22" stroke="#fff" stroke-width="2"/></svg>
      (203) 555-0183
    </p>
    <p class="centered contact__line contact__email">
      <svg width="26" height="18" viewBox="0 0 26 18" aria-label="Email"><rect x="1" y="1" width="24" height="16" fill="none" stroke="#fff" stroke-width="2"/><path d="M1 1 L13 10 L25 1" fill="none" stroke="#fff" stroke-width="2"/></svg>
      service@DrainHearth.example
    </p>
  </div>
</section>

<section class="card card--back" aria-label="Card back">
  <svg class="card__bg" viewBox="0 0 780 452" width="780" height="452" aria-hidden="true">
    <defs>
      <linearGradient id="backSilver" x1="0" y1="0" x2="1" y2="0">
        <stop offset="0" stop-color="#c9cbce"/>
        <stop offset=".35" stop-color="#fdfdfd"/>
        <stop offset=".7" stop-color="#f2f3f4"/>
        <stop offset="1" stop-color="#c4c6c9"/>
      </linearGradient>
      <linearGradient id="backBand" x1="0" y1="0" x2="0" y2="1">
        <stop offset="0" stop-color="#2f58a6"/>
        <stop offset=".3" stop-color="#123f7c"/>
        <stop offset=".7" stop-color="#1d64b0"/>
        <stop offset="1" stop-color="#3d9ee0"/>
      </linearGradient>
      <linearGradient id="backStripe" x1="0" y1="0" x2="1" y2="0">
        <stop offset="0" stop-color="#8d9094"/>
        <stop offset=".5" stop-color="#ffffff"/>
        <stop offset="1" stop-color="#8d9094"/>
      </linearGradient>
    </defs>
    <rect width="780" height="452" fill="url(#backSilver)"/>
    <path d="M0 0 L780 0 L780 116 Q390 140 0 110 Z" fill="url(#backBand)"/>
    <path d="M0 110 Q390 140 780 116 L780 128 Q390 156 0 122 Z" fill="url(#backStripe)"/>
  </svg>

  <p class="centered tagline">Fully Licensed and Insured</p>

  <ul class="centered services">
    <li>Boilers<i class="diamond"></i>Water heaters<i class="diamond"></i>Gas lines</li>
    <li>Sump pumps<i class="diamond"></i>Toilet repairs<i class="diamond"></i>Faucet repairs</li>
    <li>Pipe thawing<i class="diamond"></i>Radiant heating</li>
    <li>New construction<i class="diamond"></i>Remodels</li>
  </ul>

  <p class="centered back-web"><i class="rule"></i><span>www.<span class="domain">DrainHearth</span>.example</span><i class="rule rule--right"></i></p>
</section>

</body>
</html>
```